Business Card Design for an Investment Company

We need a business card design for our private investment company, called Ashbourne Partners. Ashbourne Partners is an investments partnership that aims to acquire shares in listed companies with a view to influencing those companies through active dialogue in order to improve their value. We need designs that use the logo colors (blue, grey, white), we need both English and Arabic on the business cards (can be on one side or 2 sides). The final logo should communicate professionalism, conservatism (nothing too fancy or too cheesy), that we are smart, conservative and old school.

Target Market(s)

Investment companies

Industry/Entity Type

Investment

Contact Information for Business Card

Khalid Yousef Rumaithi
Senior Executive Officer

Palm Terrace 07, Level 3, Office 215/12
HLMZ

+9714987650
krumaithi@ashbournepartners.com
www.ashbournepartners.com

Requirements
Must have
• Logo to be placed on the left hand side of the business card
• for the Arabic, we only need to have the name and title so it can be accomodated on one side so we can have the other side with full color and logo. The arabic that needs to be used is the below:
• خالد يوسف الرميثي
• المدير التنفيدي

```html
<!DOCTYPE html>
<html lang="en">
<head>
<meta charset="utf-8">
<title>Ashbourne Partners – Business Card</title>
<link href="https://fonts.googleapis.com/css2?family=Roboto:wght@400;500;700&family=Roboto+Condensed:wght@400;500&family=Noto+Naskh+Arabic:wght@500;600&display=swap" rel="stylesheet">
<style>
  :root {
    --backdrop: #8c8c8c;
    --card-dark: #1b1c1e;
    --card-light: #f2f2f2;
    --brand-blue: #1d6ea6;
    --panel-grey: #58585a;
    --title-grey: #555557;
    --text-white: #ffffff;
  }
  * { margin: 0; padding: 0; box-sizing: border-box; }
  html, body {
    width: 1200px; height: 960px; overflow: hidden;
    background: var(--backdrop);
    font-family: "Roboto", Arial, sans-serif;
  }
  .card {
    position: absolute; left: 320px; width: 600px;
    border-radius: 20px;
    box-shadow: 0 4px 10px rgba(0,0,0,0.35);
  }
  .card-front { top: 105px; height: 345px; background: var(--card-dark); }
  .card-back { top: 493px; height: 342px; background: var(--card-light); }

  .brand-name {
    position: absolute; left: 0; right: 0; top: 150px;
    text-align: center;
    font-weight: 700; font-size: 40px; letter-spacing: -0.5px;
    color: var(--brand-blue);
  }
  .front-web {
    position: absolute; left: 0; right: 0; top: 293px;
    text-align: center;
    font-size: 14px; letter-spacing: 4px;
    color: var(--text-white);
  }

  .holder {
    position: absolute; right: 328px; top: 112px;
    text-align: right;
    font-family: "Roboto Condensed", Arial, sans-serif;
  }
  .holder-name {
    font-weight: 500; font-size: 24px; line-height: 30px;
    color: var(--brand-blue); text-transform: uppercase;
  }
  .holder-title {
    font-weight: 500; font-size: 17px; line-height: 24px;
    color: var(--title-grey); text-transform: uppercase;
  }
  .holder-arabic {
    margin-top: 8px;
    font-family: "Noto Naskh Arabic", serif;
    direction: rtl; text-align: right;
  }
  .holder-arabic-name {
    font-weight: 600; font-size: 18px; line-height: 28px;
    color: var(--brand-blue);
  }
  .holder-arabic-title {
    font-weight: 500; font-size: 15px; line-height: 24px;
    color: var(--title-grey);
  }

  .contact-panel {
    position: absolute; left: 294px; top: 96px;
    width: 236px; height: 150px;
    background: var(--panel-grey);
    color: var(--text-white);
    padding: 13px 12px 0 22px;
    font-size: 13.5px; line-height: 20px;
  }
  .contact-address { margin-bottom: 2px; text-transform: uppercase; }
  .contact-line { display: flex; align-items: center; white-space: nowrap; }
  .contact-line svg { width: 14px; height: 14px; margin-right: 9px; flex: none; fill: var(--text-white); }
  .contact-email { font-size: 11px; letter-spacing: -0.1px; }
</style>
</head>
<body>
  <section class="card card-front">
    <div class="brand-name">Ashbourne Partners</div>
    <div class="front-web">www.ashbournepartners.com</div>
  </section>

  <section class="card card-back">
    <div class="holder">
      <div class="holder-name">Khalid Yousef Rumaithi</div>
      <div class="holder-title">Senior Executive Officer</div>
      <div class="holder-arabic" lang="ar">
        <div class="holder-arabic-name">خالد يوسف الرميثي</div>
        <div class="holder-arabic-title">المدير التنفيدي</div>
      </div>
    </div>
    <div class="contact-panel">
      <div class="contact-address">Palm Terrace 07, Level 3<br>Office 215/12, HLMZ</div>
      <div class="contact-line">
        <svg viewBox="0 0 16 16" aria-hidden="true"><path d="M3.5 1.5l2.3 2.6-1.2 1.8c.9 2 2.6 3.7 4.6 4.6l1.8-1.2 2.6 2.3-1.3 2.2C7.5 13.6 2.4 8.5 1.3 2.8z"/></svg>
        <span>+971 4 987 650</span>
      </div>
      <div class="contact-line">
        <svg viewBox="0 0 16 16" aria-hidden="true"><path d="M4 1h8v14H4zM5.5 2.5v9.5h5V2.5z"/></svg>
        <span>+971 50 412 7736</span>
      </div>
      <div class="contact-line">
        <svg viewBox="0 0 16 16" aria-hidden="true"><path d="M4 2h8v3H4zM1 6h14v6h-2v-2H3v2H1zM4 11h8v3H4z"/></svg>
        <span>+971 4 987 651</span>
      </div>
      <div class="contact-line">
        <svg viewBox="0 0 16 16" aria-hidden="true"><path d="M1 4h14v9H1zM2.2 5l5.8 4 5.8-4v-.1H2.2z"/></svg>
        <span class="contact-email">krumaithi@ashbournepartners.com</span>
      </div>
    </div>
  </section>
</body>
</html>
```